Business Card, Etc.
Bcard, Stationary and Envelope
Business Card, Etc.  - Consulting
Creative Brief
Professional
Marcus D. Fenwick
President
784 Maple Ave West Lakemont, OR 50814-2391
marcus.fenwick@tvbadvisory.com
www.tvbadvisory.com
The logo uses BankGothicBT Medium. You do not have to match the font in the logo. We might like to see a completing font. We are also going to want trading cards and a PowerPoint template when this is done!

```html
<!DOCTYPE html>
<html lang="en">
<head>
<meta charset="utf-8">
<title>TVB Advisory — Business Card</title>
<link rel="stylesheet" href="https://fonts.googleapis.com/css2?family=Open+Sans:wght@400;600;700&display=swap">
<style>
  :root {
    --navy: #1e4f73;
    --navy-deep: #173f5e;
    --paper: #ffffff;
    --ink-soft: #e6eef4;
    --stage: #eceff2;
    --rule: #c9d6e0;
  }
  * { box-sizing: border-box; margin: 0; padding: 0; }
  html, body { width: 1200px; height: 908px; overflow: hidden; }
  body {
    background: var(--stage);
    font-family: "Open Sans", Arial, sans-serif;
    display: flex;
    align-items: center;
    justify-content: center;
    gap: 48px;
  }
  .card {
    width: 530px;
    height: 303px;
    border-radius: 18px;
    overflow: hidden;
    position: relative;
    box-shadow: 0 10px 28px rgba(20, 40, 60, 0.22);
  }
  .card--front {
    background: var(--navy);
    display: flex;
    align-items: center;
    justify-content: center;
  }
  .wordmark {
    display: flex;
    align-items: center;
    gap: 12px;
    font-weight: 700;
    letter-spacing: 0.08em;
  }
  .wordmark__square { width: 22px; height: 22px; }
  .wordmark__name { font-size: 30px; text-transform: uppercase; }
  .card--front .wordmark { color: var(--paper); }
  .card--front .wordmark__square { background: var(--paper); }

  .card--back { background: var(--paper); display: flex; }
  .back__logo-panel {
    flex: 1 1 50%;
    display: flex;
    align-items: center;
    justify-content: center;
  }
  .back__logo-panel .wordmark { color: var(--navy); }
  .back__logo-panel .wordmark__name { font-size: 24px; }
  .back__logo-panel .wordmark__square { width: 18px; height: 18px; background: var(--navy); }

  .back__info-panel {
    flex: 1 1 50%;
    background: var(--navy);
    border-left: 4px solid var(--rule);
    color: var(--paper);
    padding: 34px 26px 0 28px;
  }
  .person__name { font-size: 19px; font-weight: 600; }
  .person__title { font-size: 12px; color: var(--ink-soft); margin-bottom: 14px; }
  .address { font-size: 11px; line-height: 1.45; color: var(--ink-soft); margin-bottom: 12px; }
  .contact-list { list-style: none; }
  .contact-list li {
    display: flex;
    align-items: center;
    gap: 8px;
    font-size: 11px;
    line-height: 1.9;
    color: var(--ink-soft);
    white-space: nowrap;
  }
  .contact-list svg { width: 13px; height: 13px; flex: none; }
</style>
</head>
<body>
  <section class="card card--front" aria-label="Business card front">
    <div class="wordmark">
      <span class="wordmark__square"></span>
      <span class="wordmark__name">TVB Advisory</span>
    </div>
  </section>

  <section class="card card--back" aria-label="Business card back">
    <div class="back__logo-panel">
      <div class="wordmark">
        <span class="wordmark__square"></span>
        <span class="wordmark__name">TVB Advisory</span>
      </div>
    </div>
    <div class="back__info-panel">
      <p class="person__name">Marcus D. Fenwick</p>
      <p class="person__title">President</p>
      <p class="address">784 Maple Ave West<br>Lakemont, OR 50814-2391</p>
      <ul class="contact-list">
        <li>
          <svg viewBox="0 0 16 16"><circle cx="8" cy="8" r="7.5" fill="#fff"/><path d="M5.2 4.2l1.5 1.6-.7 1.1a5 5 0 0 0 3.1 3.1l1.1-.7 1.6 1.5-.9 1.1C7.6 11.9 4.1 8.4 4.1 5.1z" fill="#1e4f73"/></svg>
          800-555-0142 (Toll Free)
        </li>
        <li>
          <svg viewBox="0 0 16 16"><circle cx="8" cy="8" r="7.5" fill="#fff"/><path d="M5.2 4.2l1.5 1.6-.7 1.1a5 5 0 0 0 3.1 3.1l1.1-.7 1.6 1.5-.9 1.1C7.6 11.9 4.1 8.4 4.1 5.1z" fill="#1e4f73"/></svg>
          541-555-0178
        </li>
        <li>
          <svg viewBox="0 0 16 16"><circle cx="8" cy="8" r="7.5" fill="#fff"/><rect x="4.5" y="6" width="7" height="5" fill="#1e4f73"/><rect x="5.8" y="3.8" width="4.4" height="2.6" fill="#1e4f73"/></svg>
          541-555-0123
        </li>
        <li>
          <svg viewBox="0 0 16 16"><circle cx="8" cy="8" r="7.5" fill="#fff"/><rect x="4" y="5.2" width="8" height="5.6" fill="none" stroke="#1e4f73" stroke-width="1.2"/><path d="M4 5.4l4 3 4-3" fill="none" stroke="#1e4f73" stroke-width="1.2"/></svg>
          marcus.fenwick@tvbadvisory.com
        </li>
        <li>
          <svg viewBox="0 0 16 16"><circle cx="8" cy="8" r="7.5" fill="#fff"/><circle cx="8" cy="8" r="4" fill="none" stroke="#1e4f73" stroke-width="1.1"/><path d="M4 8h8M8 4c-2 2.4-2 5.6 0 8M8 4c2 2.4 2 5.6 0 8" fill="none" stroke="#1e4f73" stroke-width="1"/></svg>
          www.tvbadvisory.com
        </li>
      </ul>
    </div>
  </section>
</body>
</html>
```